Business Card Design Can you design a business card design? Looking for something unique and differe

Can you design a business card design? Looking for something unique and different. Can you design a business card design? Looking for something unique and different.Can you design a business card design? Looking for something unique and different.Can you design a business card design? Looking for something unique and different.Can you design a business card design? Looking for something unique and different.Can you design a business card design? Looking for something unique and different.

Industry/Entity Type

Business

Contact Information for Business Card

Can you design a business card design? Looking for something unique and different.

Font styles to use
Serif

```html
<!DOCTYPE html>
<html lang="en">
<head>
<meta charset="utf-8">
<title>Dosewise Business Card</title>
<link rel="stylesheet" href="https://fonts.googleapis.com/css2?family=Open+Sans:wght@400;600&display=swap">
<style>
  :root {
    --backdrop: #d9d9d9;
    --card: #ffffff;
    --purple: #8a6f9e;
    --grey: #7f7f7f;
    --ink: #2a2a2a;
    --muted: #555555;
  }
  * { margin: 0; padding: 0; box-sizing: border-box; }
  html, body { width: 1200px; height: 852px; overflow: hidden; }
  body {
    background: var(--backdrop);
    font-family: "Open Sans", Arial, sans-serif;
    position: relative;
  }
  .card {
    position: absolute;
    width: 460px;
    height: 263px;
    background: var(--card);
    border-radius: 10px;
    overflow: hidden;
    box-shadow: 0 6px 18px rgba(0,0,0,0.18);
  }
  .card-front { left: 90px; top: 150px; }
  .card-back { left: 650px; top: 440px; }

  .brand { display: flex; flex-direction: column; align-items: center; position: absolute; }
  .brand-row { display: flex; align-items: center; gap: 10px; }
  .brand-mark { width: 16px; height: 16px; background: var(--purple); }
  .brand-name { color: var(--purple); font-weight: 600; letter-spacing: 0.5px; line-height: 1; }
  .brand-tagline {
    display: flex; align-items: center; gap: 8px;
    color: var(--grey); font-size: 9px; letter-spacing: 3px; margin-top: 6px;
  }
  .brand-tagline::before, .brand-tagline::after {
    content: ""; width: 40px; height: 1px; background: var(--grey);
  }
  .card-front .brand { left: 0; right: 0; top: 100px; }
  .card-front .brand-name { font-size: 44px; }

  .card-back .brand { left: 30px; top: 110px; width: 200px; }
  .card-back .brand-name { font-size: 32px; }
  .card-back .brand-tagline { font-size: 7px; letter-spacing: 2.5px; }
  .card-back .brand-tagline::before, .card-back .brand-tagline::after { width: 28px; }

  .person { position: absolute; left: 250px; top: 32px; }
  .person-name { color: var(--purple); font-weight: 600; font-size: 16px; }
  .person-title { color: var(--ink); font-size: 9px; font-style: italic; margin-top: 2px; }

  .contact-list { position: absolute; left: 250px; top: 92px; list-style: none; }
  .contact-list li {
    display: flex; align-items: center; gap: 8px;
    font-size: 11px; color: var(--ink); line-height: 17px;
  }
  .contact-list svg { width: 10px; height: 10px; fill: var(--muted); flex: none; }
  .contact-list .blank { width: 10px; flex: none; }
  .address { position: absolute; left: 250px; top: 168px; font-size: 11px; color: var(--ink); line-height: 15px; }

  .web-band {
    position: absolute; right: 0; bottom: 0; width: 210px; height: 44px;
    background: var(--purple); color: #fff; font-size: 11px;
    display: flex; align-items: center; padding-left: 24px;
  }
</style>
</head>
<body>
  <section class="card card-front">
    <div class="brand">
      <div class="brand-row">
        <span class="brand-mark"></span>
        <span class="brand-name">Dosewise</span>
      </div>
      <div class="brand-tagline">cost management</div>
    </div>
  </section>

  <section class="card card-back">
    <div class="brand">
      <div class="brand-row">
        <span class="brand-mark"></span>
        <span class="brand-name">Dosewise</span>
      </div>
      <div class="brand-tagline">cost management</div>
    </div>

    <div class="person">
      <div class="person-name">Your Long Name</div>
      <div class="person-title">Managing Director</div>
    </div>

    <ul class="contact-list">
      <li><span class="blank"></span>00.00.00.0000</li>
      <li>
        <svg viewBox="0 0 10 10"><path d="M2 1h2l1 2.5-1.2.8a5 5 0 0 0 1.9 1.9l.8-1.2L9 6v2a1 1 0 0 1-1 1A7 7 0 0 1 1 2a1 1 0 0 1 1-1z"/></svg>
        11-2222-33334
      </li>
      <li>
        <svg viewBox="0 0 10 10"><path d="M0 2h10v6H0z M0 2l5 3.5L10 2" stroke="#fff" stroke-width="0.8"/></svg>
        yourname@yourwebsite.com
      </li>
      <li>
        <svg viewBox="0 0 10 10"><circle cx="5" cy="5" r="4.5"/></svg>
        &nbsp;
      </li>
    </ul>
    <p class="address">Your Commercial or office address<br>in just two line with pincode</p>

    <div class="web-band">www.yourwebsite.com</div>
  </section>
</body>
</html>
```